Hardcore nerd needs to stand out in a sea of dull Defence business cards

Wombat Devices is a new Australian consulting engineering company that turns research and theory into practical systems. No evangelistic fluff, just mathematics and physics into electronic and optical circuits for consumer products, scientific research or Defence applications.

We already have a recognised logo (provided) which is often dark blue/black on a light background but we're open to other combinations. (Us engineers tend to have limited aesthetic imagination :)

Some of our recent products have included:
* Instrumentation for electrical testing,
* Radar jammers,
* GPS antenna design,
* Satellite tracking systems,
* High power lasers

We're open to both single and double-sided designs - happy to be convinced either way.

P.S. Another group is working on the web page, so - alas - our web site is currently of no use for images/ideas...

Target Market(s)

Engineering managers,
Scientists

Contact Information for Business Card

Dr Colin Marsh
R&D Engineer

colin@wombatdevicesco.com.au
0427 563 210

PO Box XXX (to be confirmed)
Banks ACT 2913
Australia

Font styles to use
Serif
Sans Serif

Colors

Designer to choose colors to be used in the design.

Requirements
Must have
• My contact details!
• I've had many (great) "bold and plain" designs submitted already, so feel free to be artistically creative :)
• Happy to take advice re fonts/colours/printability etc.
Nice to have
• I'm not sure if "lists" are more at home on a CV than a business card, but representative services include:
• Applied electromagnetics
• RF and high speed electronics
• Signal and image processing
• Electro-optical and laser systems
• Concept-to-prototype design services
• If you're considering double sided cards, then often measuring/alignment grids/rulers feature on the back of similar cards.
• e.g. https://www.lumoptix-example.com/newgrouppage9.cfm?objectgroup_id=4815
• https://www.lumoptix-example.com/newgrouppage9.cfm?objectgroup_ID=4817
• ..or even a "Smith chart" (google will return lots)
• Generic images to represent a capability might work - googling images associated with keyword for each of these areas might help:
• - "passive radar", "phased array", "fdtd", "vircator"
• RF and high speed electronic design
• - "smith chart", "microstrip circuits", "dimensioned drawing", "electronic schematic"
• - "dft", "iir filter"
• - "optical cavity". "laser energy level diagram"
• Background/watermarked images outlines/wireframes/schematics would probably look OK.
Should not have
• If a list of projects/services is provided, it is important not to make the client feel that this is "all" the company can do. Engineering design is a creative discipline (like graphics :)
• Please, no stock "military" snaps like planes, missiles, etc!

```html
<!DOCTYPE html>
<html lang="en">
<head>
<meta charset="utf-8">
<title>Wombat Devices – Business Card</title>
<link rel="stylesheet" href="https://fonts.googleapis.com/css2?family=PT+Sans:wght@700&display=swap">
<style>
  :root {
    --navy: #0b2266;
    --card: #f4f4f4;
    --backdrop: #8a949f;
  }
  * { margin: 0; padding: 0; box-sizing: border-box; }
  html, body {
    width: 1200px;
    height: 1200px;
    overflow: hidden;
    background: var(--backdrop);
  }
  .business-card {
    position: absolute;
    left: 100px;
    top: 310px;
    width: 1000px;
    height: 580px;
    background: var(--card);
    overflow: hidden;
    font-family: "PT Sans", "Myriad Pro", Arial, sans-serif;
    font-weight: 700;
    color: var(--navy);
    box-shadow: 0 18px 40px rgba(0,0,0,0.25);
  }
  .accent-disc {
    position: absolute;
    left: 720px;
    top: -150px;
    width: 430px;
    height: 430px;
    border-radius: 50%;
    background: var(--navy);
  }
  .brand {
    position: absolute;
    left: 60px;
    top: 52px;
    display: flex;
    align-items: center;
    gap: 18px;
  }
  .brand-mark {
    width: 56px;
    height: 56px;
    border-radius: 50%;
    background: var(--navy);
  }
  .brand-name {
    font-size: 40px;
    letter-spacing: 1px;
    text-transform: uppercase;
    line-height: 1;
  }
  .info-block {
    position: absolute;
    left: 62px;
    font-size: 31px;
    line-height: 1.2;
  }
  .person { top: 168px; }
  .contact { top: 282px; }
  .address { top: 396px; font-size: 34px; line-height: 1.18; }
  .divider {
    position: absolute;
    left: 60px;
    height: 3px;
    background: var(--navy);
  }
  .divider::after {
    content: "";
    position: absolute;
    right: -6px;
    top: -4.5px;
    width: 12px;
    height: 12px;
    border-radius: 50%;
    background: var(--navy);
  }
  .divider-one { top: 262px; width: 520px; }
  .divider-two { top: 376px; width: 610px; }
</style>
</head>
<body>
  <div class="business-card">
    <div class="accent-disc"></div>

    <div class="brand">
      <div class="brand-mark"></div>
      <div class="brand-name">Wombat Devices</div>
    </div>

    <div class="info-block person">
      <div>Dr Colin Marsh</div>
      <div>R&amp;D Engineer</div>
    </div>

    <div class="divider divider-one"></div>

    <div class="info-block contact">
      <div>colin@wombatdevicesco.com.au</div>
      <div>0427 563 210</div>
    </div>

    <div class="divider divider-two"></div>

    <div class="info-block address">
      <div>PO Box XXX (to be confirmed)</div>
      <div>Banks ACT 2913</div>
      <div>Australia</div>
    </div>
  </div>
</body>
</html>
```